Product Design Brochure Design Project

We are starting are in the process of creating a product guide for wood samples and product designs.

the two concepts that we will promote.

1: product like wood types
2: designs styles and concepts/

each concept will be on a single page... Ideally A4 sideways. i need advice as i will need to send this to a printer.

The project will require an ongoing relationship with a designer. Who can add new pages to the master document as we progress.

At its conclusion we hope to have about 40 pages maximum.

We think that it is best that we have also have PDF pages of the individual pages so we can upload those onto our webpage as downloadable PDF that relate to the product.

Essentially we need a template page with a single product for example like Pine wood and with a little explanation of the product data and large image that we have taken.

We need a price on being able to amend the document on an ongoing basis and our ability to send it to a commercial printer.

Industry/Entity Type

Printer

Requirements
Must have
• Must have ability to make changes on an ongoing basis.

```html
<!DOCTYPE html>
<html lang="en">
<head>
<meta charset="utf-8">
<title>Hartwood Decks – Brochure Cover</title>
<link rel="stylesheet" href="https://fonts.googleapis.com/css2?family=Source+Sans+3:wght@600;700&display=swap">
<style>
  :root {
    --page-bg: #ffffff;
    --plank-weathered-a: #b5824a;
    --plank-weathered-b: #a9723c;
    --plank-golden-a: #c4904c;
    --plank-golden-b: #d4a258;
    --plank-golden-c: #b98444;
    --plank-oiled-a: #c87a36;
    --plank-oiled-b: #b8602a;
    --plank-oiled-c: #c2702e;
    --plank-corner: #b4652c;
    --seam-dark: #2e1a0c;
    --seam-edge: #7a4218;
    --accent-red: #a3201f;
    --brand-tone: #8e4c1e;
    --spa-tone: #5b6f8a;
    --fire-tone: #8a5a3a;
    --yard-tone: #a89a7e;
  }
  html, body {
    margin: 0;
    padding: 0;
    width: 1200px;
    height: 900px;
    overflow: hidden;
    background: var(--page-bg);
  }
  .cover {
    position: absolute;
    left: 100px;
    top: 75px;
    width: 1000px;
    height: 707px;
    overflow: hidden;
    box-shadow: 3px 4px 6px rgba(0, 0, 0, 0.25);
  }
  .cover-art {
    position: absolute;
    inset: 0;
  }
  .tagline {
    position: absolute;
    inset: 0;
    margin: 0;
    font-family: "Source Sans 3", "Myriad Pro", sans-serif;
    font-weight: 600;
    font-size: 30px;
    line-height: 32px;
    color: var(--accent-red);
    letter-spacing: -0.4px;
  }
  .tagline span { position: absolute; white-space: nowrap; }
  .tagline .line-1 { left: 272px; top: 206px; }
  .tagline .line-2 { left: 340px; top: 239px; }
  .tagline .line-3 { left: 292px; top: 272px; }
  .brand {
    position: absolute;
    left: 526px;
    top: 512px;
    font-family: "Source Sans 3", "Myriad Pro", sans-serif;
    font-weight: 700;
    color: var(--brand-tone);
  }
  .brand-name {
    display: block;
    font-size: 94px;
    line-height: 96px;
    letter-spacing: -1px;
  }
  .brand-sub {
    display: block;
    font-size: 22px;
    line-height: 26px;
    letter-spacing: 24px;
    padding-left: 24px;
  }
</style>
</head>
<body>
  <main class="cover">
    <svg class="cover-art" width="1000" height="707" viewBox="0 0 1000 707"
         role="img" aria-label="Photograph of oiled hardwood deck boards running diagonally">
      <defs>
        <linearGradient id="plankWeathered" x1="0" y1="0" x2="1" y2="0.5">
          <stop offset="0" stop-color="var(--plank-weathered-a)"/>
          <stop offset="0.5" stop-color="var(--plank-weathered-b)"/>
          <stop offset="1" stop-color="var(--plank-weathered-a)"/>
        </linearGradient>
        <linearGradient id="plankGolden" x1="0" y1="0" x2="1" y2="0.5">
          <stop offset="0" stop-color="var(--plank-golden-c)"/>
          <stop offset="0.45" stop-color="var(--plank-golden-b)"/>
          <stop offset="0.8" stop-color="var(--plank-golden-a)"/>
          <stop offset="1" stop-color="var(--plank-golden-c)"/>
        </linearGradient>
        <linearGradient id="plankOiled" x1="0" y1="0" x2="1" y2="0.5">
          <stop offset="0" stop-color="var(--plank-oiled-b)"/>
          <stop offset="0.4" stop-color="var(--plank-oiled-a)"/>
          <stop offset="0.75" stop-color="var(--plank-oiled-c)"/>
          <stop offset="1" stop-color="var(--plank-oiled-b)"/>
        </linearGradient>
      </defs>

      <g class="deck-boards">
        <polygon class="plank plank-weathered" points="0,0 265,0 0,535" fill="url(#plankWeathered)"/>
        <polygon class="plank plank-golden" points="265,0 760,0 410,707 0,707 0,535" fill="url(#plankGolden)"/>
        <polygon class="plank plank-oiled" points="760,0 1000,0 1000,485 885,707 410,707" fill="url(#plankOiled)"/>
        <polygon class="plank plank-corner" points="1000,485 1000,707 885,707" fill="var(--plank-corner)"/>
      </g>

      <g class="board-seams">
        <polygon points="258,0 268,0 4,535 0,535 0,520" fill="var(--seam-dark)"/>
        <polygon points="752,0 764,0 414,707 401,707" fill="var(--seam-dark)"/>
        <line x1="772" y1="0" x2="424" y2="707" stroke="var(--seam-edge)" stroke-width="3" opacity="0.6"/>
        <polygon points="1000,478 1000,492 888,707 875,707" fill="var(--seam-dark)"/>
      </g>

      <g class="feature-photos" stroke="var(--accent-red)" stroke-width="2">
        <polygon class="photo-spa" points="768,61 950,61 900,183 717,183" fill="var(--spa-tone)"
                 role="img" aria-label="Photograph of a spa set into a timber deck"/>
        <polygon class="photo-firepit" points="695,197 880,197 832,317 648,317" fill="var(--fire-tone)"
                 role="img" aria-label="Photograph of a square fire pit on a lawn"/>
        <polygon class="photo-yard" points="625,333 810,333 760,455 580,455" fill="var(--yard-tone)"
                 role="img" aria-label="Photograph of a sandpit play area beneath a raised deck"/>
      </g>
    </svg>

    <h1 class="tagline">
      <span class="line-1">Canberra’s premier choice</span>
      <span class="line-2">for all your decking</span>
      <span class="line-3">and deck living needs</span>
    </h1>

    <div class="brand">
      <span class="brand-name">Hartwood</span>
      <span class="brand-sub">DECKS</span>
    </div>
  </main>
</body>
</html>
```